Business Card Design Project

We need a business card design for our company kB7 s.r.o. The company is based in Slovakia and selling massage, yoga and meditation accessories online and offline. At the place where the offices are, we have a yoga studio, massage room, show room and shop as well. We will give the business card for customers who visit our shop or show room personally and for the new suppliers of demanded products we are visiting in the future.
I would like to have:
- small logo and datas on one side
- big logo and our main e-shops on the other side:
- www.pohodlnelavice.sk
- www.relaxnipultiky.cz
Datas:
Peter Kolar, MSc. / CEO
kB7 s.r.o.
Borovicová 742/3
938 05 Lipová Dolina
Slovak republic (Slovakia)
Office tel.: +421 (0) 917 604 382
Private tel.: +421 (0) 911 758 026
E-mail: info@kb7.sk
Web: www.kb7.sk
It is up to you if you use graphics emphasizing our profile or leave it simple and modern without pics. Looking forward to receiving your designs! Thank You!

```html
<!DOCTYPE html>
<html lang="sk">
<head>
<meta charset="utf-8">
<title>kB7 s.r.o. – business card</title>
<link rel="stylesheet" href="https://fonts.googleapis.com/css2?family=Comfortaa:wght@400&family=Poiret+One&family=Lora:ital@1&display=swap">
<style>
  :root {
    --orange: #f0821e;
    --slate: #4d5966;
    --card: #f4f4f4;
    --paper-shade: #e2e2e2;
    --backdrop: #d9d6d1;
    --ink-light: #ffffff;
  }
  * { box-sizing: border-box; margin: 0; padding: 0; }
  html, body { width: 1200px; height: 900px; overflow: hidden; }
  body {
    background: var(--backdrop);
    position: relative;
    font-family: "Comfortaa", sans-serif;
  }
  .card {
    position: absolute;
    left: 250px;
    width: 700px;
    height: 400px;
    background: radial-gradient(ellipse at 40% 40%, #ffffff 0%, var(--card) 60%, var(--paper-shade) 100%);
    box-shadow: 0 6px 18px rgba(0,0,0,.18);
    overflow: hidden;
  }
  .card--details { top: 40px; }
  .card--shops { top: 460px; }

  .card__shape { position: absolute; inset: 0; }

  .brand {
    position: absolute;
    color: var(--slate);
    font-family: "Comfortaa", sans-serif;
    font-weight: 400;
    line-height: 1;
    white-space: nowrap;
  }

  .card--details .brand { left: 70px; top: 215px; font-size: 34px; }

  .holder {
    position: absolute;
    left: 70px;
    top: 290px;
    font-family: "Poiret One", sans-serif;
    font-variant: small-caps;
    letter-spacing: 3px;
    color: var(--slate);
    font-size: 30px;
    white-space: nowrap;
  }
  .holder__title { font-size: 18px; letter-spacing: 1px; }

  .contact {
    position: absolute;
    right: 34px;
    top: 34px;
    list-style: none;
    text-align: right;
    font-family: "Lora", serif;
    font-style: italic;
    color: var(--ink-light);
    font-size: 15px;
    line-height: 1.45;
  }
  .contact li { display: flex; justify-content: flex-end; align-items: flex-start; gap: 10px; }
  .contact__icon { width: 14px; height: 14px; flex: none; margin-top: 4px; }
  .contact__lines { display: block; }

  .card--shops .brand { left: 0; right: 0; top: 130px; text-align: center; font-size: 64px; }

  .shops {
    position: absolute;
    left: 0; right: 0;
    top: 265px;
    text-align: center;
    list-style: none;
    font-family: "Comfortaa", sans-serif;
    font-weight: 400;
    color: var(--slate);
    font-size: 34px;
    letter-spacing: 2px;
    line-height: 1.15;
  }
</style>
</head>
<body>

<section class="card card--details" aria-label="Card side with contact details">
  <svg class="card__shape" viewBox="0 0 700 400" aria-hidden="true">
    <rect width="700" height="400" fill="var(--orange)"/>
    <rect width="120" height="400" fill="var(--card)"/>
    <circle cx="190" cy="240" r="175" fill="var(--card)"/>
    <circle cx="430" cy="380" r="115" fill="var(--card)"/>
    <rect x="0" y="300" width="430" height="100" fill="var(--card)"/>
  </svg>

  <p class="brand">kB7 s.r.o.</p>
  <p class="holder">Peter Kolar, <span class="holder__title">MSc. / CEO</span></p>

  <ul class="contact">
    <li>
      <span class="contact__lines">kB7 s.r.o.<br>Borovicová 742/3<br>938 05 Lipová Dolina<br>Slovak republic (Slovakia)</span>
      <svg class="contact__icon" viewBox="0 0 14 14" aria-hidden="true"><path d="M7 1a4 4 0 0 0-4 4c0 3 4 8 4 8s4-5 4-8a4 4 0 0 0-4-4z" fill="#fff"/><circle cx="7" cy="5" r="1.5" fill="var(--orange)"/></svg>
    </li>
    <li>
      <span>(Office) +421 (0) 917 604 382</span>
      <svg class="contact__icon" viewBox="0 0 14 14" aria-hidden="true"><path d="M3 1l2.5 3-1.5 1.5c.8 1.8 2.2 3.2 4 4L9.5 8 12.5 10.5 11 13C6 13 1 8 1 3z" fill="#fff"/></svg>
    </li>
    <li>
      <span>(Private) +421 (0) 911 758 026</span>
      <svg class="contact__icon" viewBox="0 0 14 14" aria-hidden="true"><rect x="4" y="1" width="6" height="12" rx="1.2" fill="#fff"/><rect x="5" y="2.5" width="4" height="7" fill="var(--orange)"/></svg>
    </li>
    <li>
      <span>E-mail: info@kb7.sk</span>
      <svg class="contact__icon" viewBox="0 0 14 14" aria-hidden="true"><rect x="1" y="3" width="12" height="8" fill="#fff"/><path d="M1 3l6 5 6-5" stroke="var(--orange)" stroke-width="1" fill="none"/></svg>
    </li>
    <li>
      <span>Web: www.kb7.sk</span>
      <svg class="contact__icon" viewBox="0 0 14 14" aria-hidden="true"><circle cx="7" cy="7" r="5.5" fill="none" stroke="#fff" stroke-width="1.4"/><ellipse cx="7" cy="7" rx="2.3" ry="5.5" fill="none" stroke="#fff" stroke-width="1"/><path d="M1.5 7h11" stroke="#fff" stroke-width="1"/></svg>
    </li>
  </ul>
</section>

<section class="card card--shops" aria-label="Card side with company name and e-shops">
  <svg class="card__shape" viewBox="0 0 700 400" aria-hidden="true">
    <circle cx="60" cy="0" r="42" fill="var(--orange)"/>
    <path d="M0 10 L22 0 L40 36 L0 60 Z" fill="var(--slate)"/>
  </svg>

  <p class="brand">kB7 s.r.o.</p>

  <ul class="shops">
    <li>www.pohodlnelavice.sk</li>
    <li>www.relaxnipultiky.cz</li>
  </ul>
</section>

</body>
</html>
```